Business Card for Marco Thieblin Analytics and Marco Thieblin Photography

I want a double sided business card: on one side it should be about "Marco Thieblin Photography" and on the other side about "Marco Thieblin Analytics". You find the logos for these two projects in the attachments. The design of the business card should blend well with the colours and fonts used in the logos and should be quite simple, yet look professional and modern.

In addition to my name, there should be content for a telephone number, e-mail address and website. There should be little icons (for telephone, email and web) before these fields. I do not want a postal mail address field.
Lastly you should indicate that people can contact me in the following languages: Lëtzebuergesch, Deutsch, Français, English, Castellano, Ido
This should be very unobtrusive: either in a small muted font or with little icons (preferably without using flags as flags represent nations, not languages - one possibility would be by using the 2 letter ISO codes).

The design should be delivered in Adobe Illustrator format or something similar that I can edit easily, as it's possible that I will change my e-mail address and domain soon.

I hope this was detailed enough but still leaves you some freedom for designing something nice.

Thank you!
Marco

Industry/Entity Type

Business

Contact Information for Business Card

e-mail address: mtb_@orvenmail.example
website: www.marcothieblin.example (for Marco Thieblin Photography)
website: kelvodata.example/mtb (for Marco Thieblin Analytics - this address is likely to change)
phone: +352 691 987 654 (not my real number - I prefer not to publish it on the web)

Requirements
Nice to have
• A speech bubble followed by the 2-letter language codes (lb, de, fr, en, es, io) or even speech bubble icons for every language would be nice and eliminates the need to put text like 'you can contact me in the following languages'.

```html
<!DOCTYPE html>
<html lang="en">
<head>
<meta charset="utf-8">
<title>Marco Thieblin – Business Cards</title>
<link rel="stylesheet" href="https://fonts.googleapis.com/css2?family=Open+Sans:wght@600;700&display=swap">
<style>
  :root {
    --page-bg: #e9e4dc;
    --card-orange: #f5ad72;
    --card-green: #5fc68e;
    --panel-light: #ffffff;
    --panel-dark: #050505;
    --name-green: #4fbf85;
    --contact-white: #ffffff;
    --icon-dark: #1d3a2c;
    --lang-ink: #111111;
    --brand-orange: #e8832a;
    --brand-grey: #3a3a3a;
  }
  * { box-sizing: border-box; margin: 0; padding: 0; }
  html, body {
    width: 1200px; height: 895px; overflow: hidden;
    background: var(--page-bg);
    font-family: "Open Sans", Arial, sans-serif;
  }
  .sheet { position: relative; width: 1200px; height: 895px; }
  .card {
    position: absolute; left: 250px;
    width: 700px; height: 400px;
    border-radius: 26px; overflow: hidden;
    box-shadow: 0 6px 18px rgba(0,0,0,0.18);
  }
  .card--analytics { top: 30px; }
  .card--photography { top: 465px; }
  .card__shapes { position: absolute; inset: 0; width: 700px; height: 400px; }
  .shape-orange { fill: var(--card-orange); }
  .shape-green { fill: var(--card-green); }
  .card--analytics .shape-panel { fill: var(--panel-light); }
  .card--photography .shape-panel { fill: var(--panel-dark); }

  .brand {
    position: absolute; left: 20px; top: 100px; width: 200px;
    display: flex; flex-direction: column; align-items: center; gap: 14px;
    text-align: center;
  }
  .brand__dot { width: 54px; height: 54px; border-radius: 50%; }
  .brand__name { font-weight: 700; font-size: 21px; line-height: 1.25; }
  .card--analytics .brand__dot { background: var(--card-green); }
  .card--analytics .brand__name { color: var(--brand-grey); }
  .card--photography .brand__dot { background: var(--brand-orange); }
  .card--photography .brand__name { color: var(--brand-orange); }

  .holder-name {
    position: absolute; left: 350px; top: 36px;
    color: var(--name-green); font-weight: 700; font-size: 25px;
    letter-spacing: 2px; white-space: nowrap;
  }
  .contacts {
    position: absolute; left: 335px; top: 94px; width: 290px;
    list-style: none; color: var(--contact-white);
    font-weight: 600; font-size: 17px; letter-spacing: 0.5px;
    white-space: nowrap;
  }
  .contacts li { height: 50px; }
  .contacts .phone { font-size: 23px; letter-spacing: 2px; }

  .icons {
    position: absolute; left: 642px; top: 60px;
    display: flex; flex-direction: column; gap: 18px; align-items: center;
  }
  .icons svg { width: 36px; height: 36px; }
  .icon-fill { fill: var(--icon-dark); }
  .icon-line { fill: none; stroke: var(--icon-dark); stroke-width: 2; }
  .icon-cut { fill: var(--card-orange); }
  .icon-cut-line { fill: none; stroke: var(--card-orange); stroke-width: 2; }

  .languages {
    position: absolute; left: 330px; top: 318px;
    display: flex; align-items: center; gap: 22px;
    color: var(--lang-ink); font-weight: 600; font-size: 26px; letter-spacing: 1px;
  }
  .languages svg { width: 44px; height: 40px; }
  .bubble { fill: none; stroke: var(--lang-ink); stroke-width: 3.5; }
  .bubble-solid { fill: var(--lang-ink); }
  .bubble-dots { fill: var(--card-green); }
</style>
</head>
<body>
<main class="sheet">

  <section class="card card--analytics" aria-label="Analytics card">
    <svg class="card__shapes" viewBox="0 0 700 400" aria-hidden="true">
      <rect class="shape-orange" width="700" height="400"/>
      <path class="shape-panel" d="M0 0 H240 C205 110 220 250 330 330 L0 400 Z"/>
      <path class="shape-green" d="M0 400 C200 320 450 280 700 245 V400 Z"/>
    </svg>
    <div class="brand">
      <span class="brand__dot"></span>
      <span class="brand__name">Marco Thieblin Analytics</span>
    </div>
    <h1 class="holder-name">Marco Thieblin</h1>
    <ul class="contacts">
      <li>mtb_@orvenmail.example</li>
      <li>kelvodata.example/mtb</li>
      <li class="phone">+352 691 987 654</li>
    </ul>
    <div class="icons">
      <svg viewBox="0 0 36 36" aria-label="Email"><rect class="icon-fill" x="3" y="8" width="30" height="20" rx="2"/><path class="icon-cut-line" d="M4 9 L18 20 L32 9"/></svg>
      <svg viewBox="0 0 36 36" aria-label="Website"><circle class="icon-line" cx="18" cy="18" r="12"/><ellipse class="icon-line" cx="18" cy="18" rx="5" ry="12"/><path class="icon-line" d="M6 18 H30 M8 12 H28 M8 24 H28"/></svg>
      <svg viewBox="0 0 36 36" aria-label="Phone"><rect class="icon-fill" x="3" y="3" width="30" height="30" rx="6"/><path class="icon-cut" d="M12 9 L15 9 L17 14 L15 16 C16 19 18 21 21 22 L23 20 L28 22 L28 25 C28 27 26 28 24 28 C16 27 10 21 9 13 C9 11 10 9 12 9 Z"/></svg>
    </div>
    <div class="languages" aria-label="Languages spoken">
      <svg viewBox="0 0 44 40" aria-hidden="true"><path class="bubble" d="M18 4 C8 4 3 10 3 17 C3 22 6 26 10 28 L8 35 L16 30 C17 30 18 30 18 30"/><path class="bubble-solid" d="M20 14 H40 A3 3 0 0 1 43 17 V30 A3 3 0 0 1 40 33 H32 L26 38 L27 33 H20 A3 3 0 0 1 17 30 V17 A3 3 0 0 1 20 14 Z"/><circle class="bubble-dots" cx="24" cy="24" r="1.8"/><circle class="bubble-dots" cx="30" cy="24" r="1.8"/><circle class="bubble-dots" cx="36" cy="24" r="1.8"/></svg>
      <span>lb</span><span>de</span><span>fr</span><span>en</span><span>es</span><span>io</span>
    </div>
  </section>

  <section class="card card--photography" aria-label="Photography card">
    <svg class="card__shapes" viewBox="0 0 700 400" aria-hidden="true">
      <rect class="shape-orange" width="700" height="400"/>
      <path class="shape-panel" d="M0 0 H240 C205 110 220 250 330 330 L0 400 Z"/>
      <path class="shape-green" d="M0 400 C200 320 450 280 700 245 V400 Z"/>
    </svg>
    <div class="brand">
      <span class="brand__dot"></span>
      <span class="brand__name">Marco Thieblin Photography</span>
    </div>
    <h1 class="holder-name">Marco Thieblin</h1>
    <ul class="contacts">
      <li>mtb_@orvenmail.example</li>
      <li>www.marcothieblin.example</li>
      <li class="phone">+352 691 987 654</li>
    </ul>
    <div class="icons">
      <svg viewBox="0 0 36 36" aria-label="Email"><rect class="icon-fill" x="3" y="8" width="30" height="20" rx="2"/><path class="icon-cut-line" d="M4 9 L18 20 L32 9"/></svg>
      <svg viewBox="0 0 36 36" aria-label="Website"><circle class="icon-line" cx="18" cy="18" r="12"/><ellipse class="icon-line" cx="18" cy="18" rx="5" ry="12"/><path class="icon-line" d="M6 18 H30 M8 12 H28 M8 24 H28"/></svg>
      <svg viewBox="0 0 36 36" aria-label="Phone"><rect class="icon-fill" x="3" y="3" width="30" height="30" rx="6"/><path class="icon-cut" d="M12 9 L15 9 L17 14 L15 16 C16 19 18 21 21 22 L23 20 L28 22 L28 25 C28 27 26 28 24 28 C16 27 10 21 9 13 C9 11 10 9 12 9 Z"/></svg>
    </div>
    <div class="languages" aria-label="Languages spoken">
      <svg viewBox="0 0 44 40" aria-hidden="true"><path class="bubble" d="M18 4 C8 4 3 10 3 17 C3 22 6 26 10 28 L8 35 L16 30 C17 30 18 30 18 30"/><path class="bubble-solid" d="M20 14 H40 A3 3 0 0 1 43 17 V30 A3 3 0 0 1 40 33 H32 L26 38 L27 33 H20 A3 3 0 0 1 17 30 V17 A3 3 0 0 1 20 14 Z"/><circle class="bubble-dots" cx="24" cy="24" r="1.8"/><circle class="bubble-dots" cx="30" cy="24" r="1.8"/><circle class="bubble-dots" cx="36" cy="24" r="1.8"/></svg>
      <span>lb</span><span>de</span><span>fr</span><span>en</span><span>es</span><span>io</span>
    </div>
  </section>

</main>
</body>
</html>
```